A simple Chatterbook Ad (not Chatterbook Page) for weight loss surgery

It’s a simple ad in terms of the text.

The text should say:
Curious about weight loss surgery?
This 30 second quiz will tell you which procedure will suit you best

I'm open to variations in the text if it is thought to enhance the ad.

Targeted towards obese individuals who have been unable to lose weight with diet and exercise. My industry is weight loss surgery – webpage www.marcusbellweather.com.au. Clicking the ad leads to a quiz on my webpage relating to weight loss surgery. Most frequent users of this service are females (75%) between ages of 35 and 55 years.

Successful weight loss surgery can enable individuals who have been unable to lose weight to lose a substantial amount of the excess weight they are carrying to be healthier and happier.

```html
<!DOCTYPE html>
<html lang="en">
<head>
<meta charset="utf-8">
<title>Curious about weight loss surgery? – Marcus Bellweather</title>
<link href="https://fonts.googleapis.com/css2?family=Montserrat:wght@500;600;700;800&display=swap" rel="stylesheet">
<style>
  :root {
    --teal: #18988c;
    --teal-dark: #127a70;
    --grey: #6a6a6d;
    --white: #ffffff;
    --denim: #5b87b5;
    --denim-deep: #426d9c;
    --skin: #ecd3c4;
  }
  html, body {
    margin: 0;
    padding: 0;
    overflow: hidden;
    background: var(--white);
  }
  .ad {
    position: relative;
    width: 1200px;
    height: 1200px;
    overflow: hidden;
    background: var(--white);
    font-family: "Montserrat", sans-serif;
  }
  .hero-photo {
    position: absolute;
    left: 620px;
    top: 0;
    width: 580px;
    height: 1200px;
    background: linear-gradient(180deg, var(--skin) 0%, var(--denim) 40%, var(--denim-deep) 100%);
  }
  .headline-band {
    position: absolute;
    left: 0;
    top: 0;
    width: 1200px;
    height: 500px;
  }
  .headline {
    position: absolute;
    left: 66px;
    top: 84px;
    margin: 0;
    transform: rotate(-4.5deg);
    transform-origin: left top;
    font-weight: 800;
    line-height: 1;
  }
  .headline__curious {
    display: block;
    color: var(--white);
    font-size: 100px;
    letter-spacing: -1px;
  }
  .headline__rest {
    position: relative;
    display: block;
    padding-left: 62px;
    margin-top: 4px;
  }
  .headline__about {
    position: absolute;
    left: 0;
    top: 22px;
    width: 48px;
    height: 140px;
    background: var(--grey);
    color: var(--white);
    font-size: 32px;
    font-weight: 700;
    writing-mode: vertical-rl;
    transform: rotate(180deg);
    text-align: center;
    line-height: 48px;
  }
  .headline__topic {
    display: block;
    color: var(--grey);
    -webkit-text-stroke: 3px var(--white);
    paint-order: stroke fill;
    font-size: 90px;
    letter-spacing: -1px;
  }
  .headline__surgery {
    display: block;
    color: var(--grey);
    -webkit-text-stroke: 4px var(--white);
    paint-order: stroke fill;
    font-size: 130px;
    letter-spacing: -2px;
    margin-top: -16px;
  }
  .offer {
    position: absolute;
    left: 68px;
    top: 528px;
    margin: 0;
    font-weight: 800;
    line-height: 1;
  }
  .offer__this {
    display: block;
    color: var(--teal);
    font-size: 90px;
  }
  .offer__number {
    display: block;
    color: var(--grey);
    font-size: 150px;
    letter-spacing: -4px;
    margin-top: -2px;
  }
  .offer__unit {
    display: block;
    color: var(--grey);
    font-size: 50px;
    font-weight: 700;
    margin-top: -6px;
  }
  .offer__promise {
    display: block;
    color: var(--teal);
    font-size: 50px;
    font-weight: 700;
    line-height: 1.12;
    margin-top: 4px;
  }
  .brand {
    position: absolute;
    left: 122px;
    top: 1085px;
    display: flex;
    align-items: center;
    gap: 12px;
    color: var(--teal-dark);
    font-size: 24px;
    font-weight: 700;
  }
  .brand__mark {
    width: 30px;
    height: 30px;
    border-radius: 50%;
    background: var(--teal);
  }
  .site-link {
    position: absolute;
    left: 467px;
    top: 1072px;
    width: 626px;
    height: 58px;
    background: var(--teal);
    color: var(--white);
    font-size: 34px;
    font-weight: 500;
    line-height: 58px;
    text-align: center;
  }
</style>
</head>
<body>
  <main class="ad">
    <div class="hero-photo" role="img" aria-label="Photo of a slim woman's midriff holding out the waistband of oversized blue jeans"></div>

    <svg class="headline-band" viewBox="0 0 1200 500" aria-hidden="true">
      <polygon points="0,98 867,17 728,382 0,456" fill="var(--teal)"/>
    </svg>

    <h1 class="headline">
      <span class="headline__curious">Curious</span>
      <span class="headline__rest">
        <span class="headline__about">about</span>
        <span class="headline__topic">weight loss</span>
        <span class="headline__surgery">surgery?</span>
      </span>
    </h1>

    <p class="offer">
      <span class="offer__this">This</span>
      <span class="offer__number">30</span>
      <span class="offer__unit">second quiz</span>
      <span class="offer__promise">will tell you which<br>procedure will suit<br>you best</span>
    </p>

    <div class="brand">
      <span class="brand__mark"></span>
      <span class="brand__name">Marcus Bellweather</span>
    </div>

    <div class="site-link">www.marcusbellweather.com.au</div>
  </main>
</body>
</html>
```